BLUE HAVEN (Business Card for Training Company)

Blue Haven is a training and consultancy company with a focus on executive protection and medical. I would like the card to be nice and sharp, not overdone and in black and red. I would also like it to highlight that it is "A Dravin Company"

I would like it to be simple and highlight a few things.

1. Name
2. Title
3. Phone Number
4. Email

I would also like www.dravinholdings.example/blue-haven to be on the card somewhere.

Target Market(s)

Security Companies

Industry/Entity Type

Security

Contact Information for Business Card

Blue Haven is a training and consultancy company with a focus on executive protection and medical. I would like the card to be nice and sharp, not overdone and in black and red. I would also like it to highlight that it is "A Dravin Company" I would like it to be simple and highlight a few things. 1. Name 2. Title 3. Phone Number 4. Email I would also like www.dravinholdings.example/blue-haven to be on the card somewhere.

Requirements
Must have
• A Dravin Company listed on the card and the website
Nice to have
• Highlight Medical Training, Consultancy & Executive Protection Courses

```html
<!DOCTYPE html>
<html lang="en">
<head>
<meta charset="utf-8">
<title>Blue Haven – Business Card</title>
<link href="https://fonts.googleapis.com/css2?family=Russo+One&family=Roboto:wght@400&display=swap" rel="stylesheet">
<style>
  :root {
    --page-bg: #323232;
    --card-front-top: #1c1c1c;
    --card-front-bottom: #040404;
    --card-back: #1b1b1b;
    --brand-red: #9e1d22;
    --text-light: #e6e6e6;
    --text-soft: #d8d8d8;
    --mark-dim: #2b2b2b;
  }
  * { margin: 0; padding: 0; box-sizing: border-box; }
  html, body {
    width: 1200px; height: 1138px; overflow: hidden;
    background: var(--page-bg);
  }
  .canvas { position: relative; width: 1200px; height: 1138px; }

  .card {
    position: absolute;
    border-radius: 16px;
    overflow: hidden;
  }
  .card--front {
    left: 274px; top: 186px; width: 622px; height: 375px;
    background: linear-gradient(180deg, var(--card-front-top) 0%, #0c0c0c 55%, var(--card-front-bottom) 100%);
  }
  .card--back {
    left: 276px; top: 608px; width: 618px; height: 374px;
    background: var(--card-back);
  }

  .wordmark {
    position: absolute;
    font-family: "Russo One", sans-serif;
    text-transform: uppercase;
    line-height: 0.92;
    letter-spacing: 1px;
  }
  .wordmark--front {
    left: 0; right: 0; top: 108px;
    text-align: center;
    font-size: 72px;
    color: var(--mark-dim);
  }
  .wordmark--back {
    left: 54px; top: 136px;
    font-size: 50px;
    color: var(--text-light);
  }

  .front-url {
    position: absolute; left: 0; right: 0; top: 332px;
    display: flex; justify-content: center; align-items: center; gap: 14px;
    font-family: "Roboto", sans-serif; font-size: 16px; color: var(--text-soft);
    white-space: nowrap;
  }
  .front-url svg { width: 48px; height: 8px; }

  .contact {
    position: absolute; left: 296px; top: 104px;
    font-family: "Roboto", sans-serif; color: var(--text-soft);
    white-space: nowrap;
  }
  .contact__name {
    font-family: "Russo One", sans-serif;
    font-size: 24px; color: var(--brand-red); letter-spacing: 0.5px;
    line-height: 1.1;
  }
  .contact__title { font-size: 15px; line-height: 20px; margin-top: 4px; }
  .contact__list { list-style: none; margin-top: 14px; }
  .contact__item {
    display: flex; align-items: center;
    height: 23px; line-height: 23px; font-size: 14px;
  }
  .contact__item svg { width: 14px; height: 14px; margin-left: 2px; margin-right: 14px; flex: none; }

  .parent-company {
    margin-top: 12px;
    display: flex; align-items: center; gap: 7px;
    font-family: "Russo One", sans-serif; font-size: 14px;
    color: var(--text-light); letter-spacing: 1px; text-transform: uppercase;
  }
  .parent-company__square {
    width: 12px; height: 12px; background: var(--brand-red);
  }
</style>
</head>
<body>
<main class="canvas">

  <section class="card card--front" aria-label="Card front">
    <div class="wordmark wordmark--front">Blue<br>Haven</div>
    <p class="front-url">
      <svg viewBox="0 0 48 8" aria-hidden="true"><line x1="4" y1="4" x2="48" y2="4" stroke="#d8d8d8" stroke-width="1.5"/><path d="M0 4 L10 1.5 L10 6.5 Z" fill="#d8d8d8"/></svg>
      <span>www.dravinholdings.example/blue-haven</span>
      <svg viewBox="0 0 48 8" aria-hidden="true"><line x1="0" y1="4" x2="44" y2="4" stroke="#d8d8d8" stroke-width="1.5"/><path d="M48 4 L38 1.5 L38 6.5 Z" fill="#d8d8d8"/></svg>
    </p>
  </section>

  <section class="card card--back" aria-label="Card back">
    <div class="wordmark wordmark--back">Blue<br>Haven</div>

    <div class="contact">
      <h1 class="contact__name">OWEN HALE</h1>
      <p class="contact__title">Managing Director</p>
      <ul class="contact__list">
        <li class="contact__item">
          <svg viewBox="0 0 14 14" aria-hidden="true"><path d="M1 5 Q7 0 13 5 L11 7 L9 5.5 L5 5.5 L3 7 Z M3 8 H11 L12 13 H2 Z" fill="var(--brand-red)"/></svg>
          <span>555-014-2290</span>
        </li>
        <li class="contact__item">
          <svg viewBox="0 0 14 14" aria-hidden="true"><rect x="1" y="3" width="12" height="8" fill="var(--brand-red)"/><path d="M1 3 L7 8 L13 3" fill="none" stroke="#1b1b1b" stroke-width="1"/></svg>
          <span>info@dravinholdings.example</span>
        </li>
        <li class="contact__item">
          <svg viewBox="0 0 14 14" aria-hidden="true"><circle cx="7" cy="7" r="5.5" fill="none" stroke="var(--brand-red)" stroke-width="1.3"/><ellipse cx="7" cy="7" rx="2.4" ry="5.5" fill="none" stroke="var(--brand-red)" stroke-width="1"/><line x1="1.5" y1="7" x2="12.5" y2="7" stroke="var(--brand-red)" stroke-width="1"/></svg>
          <span>www.dravinholdings.example/blue-haven</span>
        </li>
      </ul>
      <p class="parent-company"><span class="parent-company__square" aria-hidden="true"></span>A Dravin Company</p>
    </div>
  </section>

</main>
</body>
</html>
```